Woman owned consulting company needs an elegant and modern business card design

I need a business card design for my new consulting company, Mara Quill Consulting. I am looking for something that is simple and elegant, but also creative and original. You can use either version of the logo that are attached. I have also included the information that needs to be featured on the business card.

Requirements
Must have
• The logo and the font type and a standard business card size. Use shades of gray/silver and or rose gold that are in the logo.
• I didn't realize that my actual logo wasn't attached. Please incorporate in the designs.
Should not have
• Colors that are different from my logo

```html
<!DOCTYPE html>
<html lang="en">
<head>
<meta charset="utf-8">
<title>Mara Quill Consulting – Business Cards</title>
<link rel="stylesheet" href="https://fonts.googleapis.com/css2?family=Cinzel:wght@400;500&display=swap">
<style>
  :root {
    --backdrop: #a8a8a8;
    --card-cobalt: #3e5479;
    --foil-silver: #dfe3e8;
    --foil-soft: #c9ced6;
  }
  * { box-sizing: border-box; margin: 0; padding: 0; }
  html, body {
    width: 1200px;
    height: 1016px;
    overflow: hidden;
    background: var(--backdrop);
  }
  .canvas {
    position: relative;
    width: 1200px;
    height: 1016px;
  }
  .card {
    position: absolute;
    left: 332px;
    width: 549px;
    height: 314px;
    background: var(--card-cobalt);
    font-family: "Cinzel", serif;
    color: var(--foil-silver);
    text-align: center;
  }
  .card--front { top: 131px; }
  .card--back  { top: 514px; }

  .front-name {
    position: absolute;
    top: 88px;
    left: 0;
    width: 100%;
    font-size: 29px;
    font-weight: 500;
    letter-spacing: 1px;
    line-height: 1;
  }
  .front-title {
    position: absolute;
    top: 127px;
    left: 0;
    width: 100%;
    font-size: 11px;
    letter-spacing: 14px;
    padding-left: 14px;
    color: var(--foil-soft);
  }
  .front-rule {
    position: absolute;
    top: 161px;
    left: 232px;
    width: 86px;
    height: 2px;
  }
  .front-phone {
    position: absolute;
    top: 186px;
    left: 0;
    width: 100%;
    font-size: 12px;
    letter-spacing: 0.5px;
  }
  .front-web {
    position: absolute;
    top: 207px;
    left: 0;
    width: 100%;
    font-size: 12.5px;
    letter-spacing: 0.6px;
  }

  .back-name {
    position: absolute;
    top: 142px;
    left: 0;
    width: 100%;
    font-size: 27px;
    font-weight: 500;
    letter-spacing: 2px;
    line-height: 1;
  }
</style>
</head>
<body>
<main class="canvas">
  <section class="card card--front" aria-label="Business card front">
    <h1 class="front-name">MARA QUILL</h1>
    <p class="front-title">OWNER</p>
    <svg class="front-rule" viewBox="0 0 86 2" preserveAspectRatio="none" aria-hidden="true">
      <defs>
        <linearGradient id="rule-fade" x1="0" x2="1">
          <stop offset="0" stop-color="#dfe3e8" stop-opacity="0"/>
          <stop offset="0.5" stop-color="#dfe3e8" stop-opacity="1"/>
          <stop offset="1" stop-color="#dfe3e8" stop-opacity="0"/>
        </linearGradient>
      </defs>
      <rect width="86" height="2" fill="url(#rule-fade)"/>
    </svg>
    <p class="front-phone">610-555-0142</p>
    <p class="front-web">WWW.MARAQUILLCONSULTING.COM</p>
  </section>

  <section class="card card--back" aria-label="Business card back">
    <p class="back-name">MARA QUILL CONSULTING</p>
  </section>
</main>
</body>
</html>
```